Sexy stockings - 1 creative web page design needed!

We need a design for the main home page of our company 'Calloway Hosiery'. Out company sells stockings for women in Australia and this will be an online shopping site.

I have mocked up an example showing the type of layout and text that is required:
http://www.callowayhosiery.example.au

The design should have the same menu and text as shown in the example. A slider will be positioned in the middle of the page promoting certain styles.

The page currently has a width of 800px.

What I am looking for is some genuine design flare. Good use of fonts, stylish menu and interesting background. Also please note, this is the will be the home page so please keep text to a minimum.

An example of stylish menus can be seen here: (See 22, 26, 41)
http://brightpalette.example.com/design-showcase-inspiration/50-stylish-navigation-menus-for-design-inspiration/

An example of creative footers:
http://www.trelvomag.example.com/2009/01/40-nice-and-creative-website-footer-designs/

(See 22, 26, 41)

Update: I would like a banner picture at the top with the logo and title overlaid. Also some areas where I could advertise specials and 1 day delivery in the Metro area.

Only one page is required to be designed. No coding of links, slider etc is needed.

The deliverable will be one photoshop project file.
Updates

So far the designs submitted have not been very creative. I am not interested in a plain design where you have just copy and pasted the pictures I  have supplied and changed the background colour - I could do this myself in Photoshop. What I am looking for is some genuine design flare. Good use of fonts, stylish menu and interesting background.

Also note - this is a home page, so there should be minimal text. 

Once a quality design has been submitted, I will guarantee this project.

Reason: I have extended the deadline in order for designers to submit their new designs for the following update to the brief: I have decided a banner picture at the top with the logo and title overlaid would look great. Also can I have some areas on the page where I could advertise specials and 1 day delivery in the Metro area.

I have now guaranteed the project.

Target Market(s)

We are marketing this product to the sophisticated professional woman.

Industry/Entity Type

Online Shopping

Requirements
Must have
• Must have the subtitle - "Signature Italian Stockings"

Logo picture incorporated somewhere on page. (Do not include "Sheer Silky Stockings" from packaging.)

The style of the webpage should be consistent with the packaging.

Please see the attached files.
Nice to have
• A creative background pattern - maybe incorporate the logo.
Should not have
• I am looking for a CREATIVE design, do not submit a design that has is just the supplied pictures copy and pasted in a different layout. (I could easily do that myself).

```html
<!DOCTYPE html>
<html lang="en">
<head>
<meta charset="utf-8">
<title>Calloway Hosiery – Signature Italian Stockings</title>
<link href="https://fonts.googleapis.com/css2?family=Libre+Baskerville:wght@400;700&family=Arimo:wght@400;700&display=swap" rel="stylesheet">
<style>
  :root{
    --bg-dark:#56555b;
    --bg-dark-2:#4a494f;
    --rose:#c4969c;
    --rose-light:#f3c9cd;
    --rose-pale:#f7dadd;
    --rose-text:#e9b7bd;
    --ink:#4a3d40;
    --panel:#ffffff;
    --ribbon-top:#5e5d63;
    --ribbon-mid:#77767c;
    --footer-top:#f6d3d6;
    --footer-bot:#eab7bd;
    --footer-ink:#5b4a4e;
  }
  *{box-sizing:border-box;margin:0;padding:0}
  html,body{width:1200px;height:834px;overflow:hidden}
  body{
    position:relative;
    background:linear-gradient(180deg,var(--bg-dark) 0%,var(--bg-dark-2) 100%);
    font-family:"Libre Baskerville",Georgia,serif;
  }
  .brand{position:absolute;left:150px;top:20px;width:190px;text-align:center}
  .brand-mark{width:78px;height:78px;border-radius:50%;background:var(--rose-light);margin:0 auto 14px}
  .brand-name{font-size:34px;color:#fff;font-weight:400;line-height:1}
  .brand-tagline{font-family:"Arimo",Arial,sans-serif;font-size:9px;letter-spacing:1.4px;color:var(--rose-text);margin-top:8px;font-weight:700}

  .cart-bar{position:absolute;left:358px;top:46px;width:720px;height:24px;background:var(--rose);border-bottom:1px solid #a97c82}
  .cart-info{position:absolute;right:86px;top:5px;font-family:"Arimo",Arial,sans-serif;font-size:12px;color:#fff;display:flex;align-items:center;gap:6px}
  .cart-btn{position:absolute;right:0;top:0;height:24px;width:72px;background:var(--rose-pale);font-family:"Arimo",Arial,sans-serif;font-size:12px;font-weight:700;color:var(--ink);text-align:center;line-height:24px}

  .main-nav{position:absolute;left:370px;top:46px}
  .nav-active{position:absolute;left:0;top:0;width:96px;height:92px;background:linear-gradient(180deg,#6a696f,#4c4b51);border:1px solid var(--rose);border-top:none}
  .nav-item{position:absolute;top:38px;font-size:13px;color:#fff;white-space:nowrap}
  .nav-item.is-current{left:0;width:96px;text-align:center;color:var(--rose-text);font-size:12.5px}

  .content-panel{position:absolute;left:120px;top:190px;width:960px;height:552px;background:var(--panel);box-shadow:0 0 10px rgba(0,0,0,.35)}

  .specials{position:absolute;left:139px;top:209px;width:211px;height:398px}
  .specials svg{position:absolute;left:0;top:0}
  .specials-title{position:absolute;top:16px;width:100%;text-align:center;color:var(--rose-text);font-size:16px}
  .specials-list{position:absolute;top:58px;width:100%;list-style:none;text-align:center}
  .specials-list li{color:#fff;font-size:13.5px;line-height:18px;height:70px;text-shadow:0 1px 1px rgba(0,0,0,.4)}
  .specials-dot{position:absolute;left:82px;top:272px;width:48px;height:48px;border-radius:50%;background:var(--rose-light)}

  .delivery{position:absolute;left:148px;top:634px;width:195px;height:92px;background:linear-gradient(180deg,#f8cfd3,#eeb7bd);box-shadow:0 2px 5px rgba(0,0,0,.25);padding:6px}
  .delivery-inner{border:1px solid #c99ca1;height:100%;display:flex;align-items:center;justify-content:center;text-align:center;font-weight:700;font-size:13px;line-height:20px;color:var(--ink)}

  .slider{position:absolute;left:372px;top:209px;width:689px;height:516px;border:1px solid #d8a7ad}
  .slide-image{position:absolute;inset:0;background:radial-gradient(ellipse at 65% 45%,#e4c7b4 0%,#b88a78 30%,#6b2c2e 62%,#2f2a22 100%)}
  .slider-arrow{position:absolute;top:237px;width:36px;height:34px;background:rgba(255,255,255,.35)}
  .slider-arrow.prev{left:0}
  .slider-arrow.next{right:0}
  .slider-dots{position:absolute;left:10px;bottom:8px;display:flex;gap:8px}
  .slider-dots span{width:10px;height:10px;background:#fff}
  .slider-dots span.is-active{background:var(--rose-light)}

  .site-footer{position:absolute;left:0;top:744px;width:1200px;height:90px;background:linear-gradient(180deg,var(--footer-top),var(--footer-bot));border-top:2px solid #fbe4e6;font-family:"Arimo",Arial,sans-serif;color:var(--footer-ink)}
  .footer-col{position:absolute;top:18px;border-left:1px solid #9b8084;padding-left:10px;list-style:none;font-size:12px;line-height:19px;height:60px}
  .footer-col:nth-child(1){left:367px}
  .footer-col:nth-child(2){left:470px}
  .footer-col:nth-child(3){left:589px}
  .footer-brand{position:absolute;right:142px;top:24px;text-align:right;font-size:11px;line-height:13px}
  .footer-brand strong{font-size:12px}
  .footer-copy{margin-top:10px;font-size:10.5px}
</style>
</head>
<body>
  <header>
    <div class="brand">
      <div class="brand-mark"></div>
      <div class="brand-name">Calloway</div>
      <div class="brand-tagline">Signature Italian Stockings</div>
    </div>

    <div class="cart-bar">
      <div class="cart-info">
        <svg width="16" height="13" viewBox="0 0 16 13"><path d="M0 1h3l2 7h8l2-5H4.5" fill="none" stroke="#4a3d40" stroke-width="1.6"/><circle cx="6" cy="11" r="1.4" fill="#4a3d40"/><circle cx="12" cy="11" r="1.4" fill="#4a3d40"/></svg>
        <span>0 Items</span>
      </div>
      <div class="cart-btn">View Cart</div>
    </div>

    <nav class="main-nav">
      <div class="nav-active"></div>
      <span class="nav-item is-current">COLLECTION</span>
      <span class="nav-item" style="left:145px">NEWS</span>
      <span class="nav-item" style="left:242px">ABOUT</span>
    </nav>
  </header>

  <main class="content-panel"></main>

  <aside class="specials">
    <svg width="211" height="398" viewBox="0 0 211 398">
      <defs>
        <radialGradient id="ribbonShade" cx="50%" cy="55%" r="70%">
          <stop offset="0" stop-color="var(--ribbon-mid)"/>
          <stop offset="1" stop-color="var(--ribbon-top)"/>
        </radialGradient>
      </defs>
      <path d="M0 0H211V398L105.5 348L0 398Z" fill="url(#ribbonShade)"/>
      <path d="M5 0V386L105.5 340L206 386V0" fill="none" stroke="#d9a4aa" stroke-width="1"/>
    </svg>
    <h2 class="specials-title">CALLOWAY SPECIALS</h2>
    <ul class="specials-list">
      <li>Winter Collection<br>2011</li>
      <li>Spring Collection<br>2011</li>
      <li>Summer Collection<br>2012</li>
    </ul>
    <div class="specials-dot"></div>
  </aside>

  <div class="delivery"><div class="delivery-inner">One Day Delivery in<br>the Metro Area.</div></div>

  <section class="slider">
    <div class="slide-image" role="img" aria-label="Promotional photo of a woman in a blush tulle slip and sheer fishnet stockings seated in a red velvet armchair beside ferns"></div>
    <div class="slider-arrow prev"><svg width="36" height="34" viewBox="0 0 36 34"><path d="M21 8L12 17L21 26" fill="none" stroke="#fff" stroke-width="2"/></svg></div>
    <div class="slider-arrow next"><svg width="36" height="34" viewBox="0 0 36 34"><path d="M15 8L24 17L15 26" fill="none" stroke="#fff" stroke-width="2"/></svg></div>
    <div class="slider-dots"><span class="is-active"></span><span></span><span></span><span></span><span></span></div>
  </section>

  <footer class="site-footer">
    <ul class="footer-col"><li>Collection</li><li>News</li><li>About</li></ul>
    <ul class="footer-col"><li>Shopping Cart</li><li>Shipping</li><li>Returns</li></ul>
    <ul class="footer-col"><li>Privacy Policy</li><li>Site Map</li><li>Contact</li></ul>
    <div class="footer-brand">
      <strong>Calloway Hosiery</strong><br>Signature Italian Stockings
      <div class="footer-copy">© Copyright 2012 Calloway Hosiery</div>
    </div>
  </footer>
</body>
</html>
```